new dating app design - young, fresh, clean

Project Brief

Zivvo is the world's first dating app that actually arranges dates. The process consists of 3 easy steps:

1. use our calendar to tell us when you'd like a date
2. browse singles nearby and select who you'd like to meet
3. when your date is 1 hour away, the app will find you a nice venue in the neighborhood and send one of your matches there to meet you. All you need to do is show up and have a good time.

This design assignment consists of creating a fun, fresh & user-friendly design for the wireframes created by our UX designer. Included are 2 screens:

1. the 'calendar' screen

2. the 'matches' screen

Also included is our style guide for your reference. Feel free to use as much or as little from this guide as you please. It would be nice if we could remain somewhat consistent with our previous design (which was purely based on this style guide) but we also want you to be creative and show off your skills so by no means should you feel obliged to conform to it.

Things to consider

1. 'calendar'

this is where you tell the app when you're free for a date. You can select as many time slots as you want. The info bars at the top and the bottom are 'sticky' (will stay in place no matter where in the screen you scroll to).

Everything about this page needs to be designed: not just in terms of spacing, font and coloring of the calendar itself but also the sticky bars at the bottom and top, and the interactions (when you select a time slot, what happens visually? How will it show that this slot was selected?).

TIP: please ignore the black vs white time slot distribution you see in the image. This was meant to signify where daytime becomes nighttime and vice versa, but we're not doing that anymore. So the only difference between blocks will be the difference between a selected and an unselected block. Make sure that difference is clearly visible in your design.

2. 'matches'

this is where you tell the app whom you'd like to meet with. You can select as many people as you want by clicking their 'heart' icon. You can scroll down to see more people and again the info bars at the top and/or bottom are sticky. The design elements for this page are:

a. the page itself (sizing, spacing of the images, etc.)
b. the interactions (how does a selected heart look, how does that compare to an unselected heart)

ICONS: feel free to come up with your own iconography (ie for the 'chat' icon in the top right, and/or the 'heart' icon signifying you want to meet this person. We really like the fact that the 'matches' and 'calendar' tabs are signified with words rather than icons, but feel free to get creative on this front as well. If you can make it prettier, we're all ears :) Whatever you do on this front, make sure all your icons and the rest of your work are/is free of copyright so we can actually use them in a commercially distributed app.

The winner of this contest may get awarded a follow-up project where they will be asked to design the entire app for us.

Reason: Thank you all for your submissions. We got some promising designs but nothing that was good enough just yet. We gave some feedback for improvement and wanted to give you guys some more time to get it right. New submissions are welcome too of course. Don't hesitate to contact us if you have any questions.

Target Market(s)

singles

Industry/Entity Type

Dating

Requirements
Must have
• fresh, clean, user-friendly design of the 2 pages provided. Your design choices should include decisions about font, sizing, colours, spacing, etc.
Nice to have
• custom icons, see project brief

```html
<!DOCTYPE html>
<html lang="en">
<head>
<meta charset="utf-8">
<title>Zivvo Home – Schedule</title>
<link href="https://fonts.googleapis.com/css2?family=Roboto:wght@400;500&display=swap" rel="stylesheet">
<style>
  :root {
    --brand-red: #d84f5b;
    --brand-red-light: #e0636d;
    --accent-yellow: #f3d54a;
    --tab-inactive: #f3b3b8;
    --white: #ffffff;
    --info-bg: #f1f1f1;
    --info-text: #6f6f6f;
    --slot-text: #7c7c7c;
    --slot-label: #8a8a8a;
    --grid-line: #e6e6e6;
    --selected-bg: #fbe8e9;
    --selected-text: #e0525f;
  }
  * { box-sizing: border-box; margin: 0; padding: 0; }
  html, body { width: 675px; height: 1200px; overflow: hidden; background: var(--white); }
  body { font-family: "Roboto", Arial, sans-serif; position: relative; }

  .app-header {
    position: absolute; top: 0; left: 0; width: 675px; height: 212px;
    background: radial-gradient(ellipse at 50% 40%, var(--brand-red-light), var(--brand-red) 70%);
    color: var(--white);
    box-shadow: 0 2px 4px rgba(0,0,0,0.12);
    z-index: 2;
  }
  .status-bar { position: absolute; top: 0; left: 0; width: 100%; height: 40px; }
  .status-time { position: absolute; top: 10px; left: 0; width: 100%; text-align: center; font-size: 15px; font-weight: 500; }
  .status-battery-label { position: absolute; top: 10px; left: 589px; font-size: 15px; font-weight: 500; }

  .title-bar { position: absolute; top: 62px; left: 0; width: 100%; height: 48px; }
  .app-title { position: absolute; top: 8px; left: 0; width: 100%; text-align: center; font-size: 26px; font-weight: 500; letter-spacing: 0.3px; }
  .icon { position: absolute; }
  .icon-menu { left: 24px; top: 14px; }
  .icon-chat { left: 533px; top: 6px; }
  .icon-info { left: 615px; top: 6px; }

  .tabs { position: absolute; top: 150px; left: 0; width: 100%; height: 62px; display: flex; }
  .tab { flex: 1; text-align: center; font-size: 22px; font-weight: 500; line-height: 42px; position: relative; }
  .tab-matches { color: var(--tab-inactive); }
  .tab-schedule { color: var(--white); }
  .tab-schedule::after { content: ""; position: absolute; left: 0; right: 0; bottom: 0; height: 3px; background: var(--accent-yellow); }

  .info-top {
    position: absolute; top: 212px; left: 0; width: 675px; height: 90px;
    background: var(--info-bg); color: var(--info-text);
    font-size: 18px; font-weight: 500; line-height: 33px; padding: 11px 26px 0;
    border-bottom: 1px solid var(--grid-line);
  }

  .slot-grid {
    position: absolute; top: 302px; left: 0; width: 675px;
    display: grid; grid-template-columns: repeat(4, 1fr); grid-auto-rows: 80.2px;
  }
  .slot {
    position: relative; display: flex; align-items: center; justify-content: center;
    font-size: 30px; color: var(--slot-text);
    border-right: 1px solid var(--grid-line); border-bottom: 1px solid var(--grid-line);
    padding-top: 2px;
  }
  .slot:nth-child(4n) { border-right: none; }
  .slot.is-selected { background: var(--selected-bg); color: var(--selected-text); }
  .slot-day { position: absolute; top: 5px; left: 0; width: 100%; text-align: center; font-size: 15px; color: var(--slot-label); }
  .slot.has-day { padding-top: 24px; align-items: flex-start; }
  .slot.has-day .slot-time { margin-top: 0; }

  .info-bottom {
    position: absolute; top: 1104px; left: 0; width: 675px; height: 96px;
    background: var(--info-bg); color: var(--info-text);
    font-size: 19.5px; font-weight: 500; line-height: 33px; text-align: center; padding-top: 15px;
    box-shadow: 0 -2px 4px rgba(0,0,0,0.08);
    z-index: 2;
  }
</style>
</head>
<body>
  <header class="app-header">
    <div class="status-bar">
      <svg class="icon" style="left:10px;top:14px" width="100" height="14" viewBox="0 0 100 14">
        <g fill="#fff">
          <circle cx="5" cy="6" r="4"/><circle cx="15" cy="6" r="4"/><circle cx="25" cy="6" r="4"/><circle cx="35" cy="6" r="4"/><circle cx="45" cy="6" r="4"/>
        </g>
        <g fill="none" stroke="#fff" stroke-width="2" stroke-linecap="round">
          <path d="M60 5 Q69 -2 78 5"/><path d="M63 8 Q69 3 75 8"/>
        </g>
        <circle cx="69" cy="11" r="1.8" fill="#fff"/>
      </svg>
      <div class="status-time">9:41 PM</div>
      <svg class="icon" style="left:574px;top:11px" width="12" height="18" viewBox="0 0 12 18">
        <path d="M2 5 L10 12 L6 16 L6 2 L10 6 L2 13" fill="none" stroke="#fff" stroke-width="1.5" stroke-linejoin="round"/>
      </svg>
      <div class="status-battery-label">100%</div>
      <svg class="icon" style="left:633px;top:12px" width="34" height="16" viewBox="0 0 34 16">
        <rect x="1" y="1" width="28" height="13" rx="3" fill="none" stroke="#fff" stroke-width="1.5"/>
        <rect x="3" y="3" width="24" height="9" rx="1.5" fill="#fff"/>
        <rect x="30.5" y="5" width="2" height="5" rx="1" fill="#fff"/>
      </svg>
    </div>

    <div class="title-bar">
      <svg class="icon icon-menu" width="34" height="24" viewBox="0 0 34 24">
        <g stroke="#fff" stroke-width="3" stroke-linecap="round">
          <line x1="2" y1="2" x2="32" y2="2"/><line x1="2" y1="12" x2="32" y2="12"/><line x1="2" y1="22" x2="32" y2="22"/>
        </g>
      </svg>
      <div class="app-title">ZIVVO HOME</div>
      <svg class="icon icon-chat" width="48" height="40" viewBox="0 0 48 40">
        <path d="M24 6 Q30 0 37 3 Q45 7 42 16 Q41 20 44 24 Q38 23 35 21" fill="none" stroke="#fff" stroke-width="2.5" stroke-linecap="round"/>
        <ellipse cx="19" cy="24" rx="17" ry="12" fill="#fff"/>
        <path d="M6 30 L3 38 L13 33 Z" fill="#fff"/>
        <g fill="var(--brand-red)">
          <circle cx="12" cy="24" r="2"/><circle cx="19" cy="24" r="2"/><circle cx="26" cy="24" r="2"/>
        </g>
      </svg>
      <svg class="icon icon-info" width="38" height="38" viewBox="0 0 38 38">
        <circle cx="19" cy="19" r="17" fill="none" stroke="#fff" stroke-width="2.8"/>
        <circle cx="19" cy="11" r="2.2" fill="#fff"/>
        <rect x="17.4" y="16" width="3.2" height="13" rx="1" fill="#fff"/>
      </svg>
    </div>

    <nav class="tabs">
      <div class="tab tab-matches">MATCHES</div>
      <div class="tab tab-schedule">SCHEDULE</div>
    </nav>
  </header>

  <div class="info-top">CHOOSE WHEN YOU'RE AVAILABLE. WE'LL SCHEDULE YOUR DATES FOR YOU!</div>

  <main class="slot-grid">
    <div class="slot has-day"><span class="slot-day">Today</span><span class="slot-time">13:00</span></div>
    <div class="slot">14:00</div><div class="slot">15:00</div><div class="slot">16:00</div>
    <div class="slot">17:00</div><div class="slot">18:00</div><div class="slot is-selected">19:00</div><div class="slot">20:00</div>
    <div class="slot">21:00</div><div class="slot">22:00</div><div class="slot">23:00</div>
    <div class="slot has-day"><span class="slot-day">Tomorrow</span><span class="slot-time">00:00</span></div>
    <div class="slot">01:00</div><div class="slot">02:00</div><div class="slot">03:00</div><div class="slot">04:00</div>
    <div class="slot">05:00</div><div class="slot">06:00</div><div class="slot">07:00</div><div class="slot">08:00</div>
    <div class="slot">09:00</div><div class="slot">10:00</div><div class="slot">11:00</div><div class="slot">12:00</div>
    <div class="slot">13:00</div><div class="slot">14:00</div><div class="slot">15:00</div><div class="slot">16:00</div>
    <div class="slot">17:00</div><div class="slot">18:00</div><div class="slot">19:00</div><div class="slot">20:00</div>
    <div class="slot">21:00</div><div class="slot">22:00</div><div class="slot">23:00</div>
    <div class="slot has-day"><span class="slot-day">Friday</span><span class="slot-time">00:00</span></div>
    <div class="slot">01:00</div><div class="slot">02:00</div><div class="slot">03:00</div><div class="slot">04:00</div>
  </main>

  <footer class="info-bottom">SELECT THE ONE HOUR BLOCKS IN WHICH YOU'RE AVAILABLE<br>TO MEET UP WITH YOUR MATCHES.</footer>
</body>
</html>
```